Rivex Management LLC Business Card

The sample logo was attached for the business Card Design for Traffic Control Company named Rivex Management LLC. Card design needs to have the company logo and colors match the logo color. It will be nice to show some images of Traffic control signs or cones, even roads closer that math the company services

Target Market(s)

Temporary traffic control. Road closer.

Industry/Entity Type

Construction

Contact Information for Business Card

basic information, name, job title, address, email phone, website

Font styles to use
Serif
Sans Serif

Colors
F0912C
F2A743
F7CA91
FBE8D2
FDF5EE
EE7325
F08F49
F5BC92
FAE3D3
FDF4ED

```html
<!DOCTYPE html>
<html lang="en">
<head>
<meta charset="utf-8">
<title>Rivex Management LLC Business Card</title>
<link rel="stylesheet" href="https://fonts.googleapis.com/css2?family=Montserrat:wght@400;500;700&display=swap">
<style>
  :root {
    --backdrop: #d9d9db;
    --card: #1c1c1e;
    --orange: #ee7325;
    --text-light: #c9c9c9;
    --text-muted: #9a9a9a;
    --divider: #4a4a4c;
  }
  * { margin: 0; padding: 0; box-sizing: border-box; }
  html, body { width: 1200px; height: 800px; overflow: hidden; }
  body {
    background: var(--backdrop);
    font-family: "Montserrat", sans-serif;
    display: flex;
    align-items: center;
    justify-content: center;
    gap: 40px;
  }
  .card {
    width: 540px;
    height: 309px;
    background: var(--card);
    border-radius: 18px;
    border-bottom: 4px solid var(--orange);
    border-right: 2px solid var(--orange);
    position: relative;
    overflow: hidden;
  }
  /* contact side */
  .identity {
    position: absolute;
    right: 290px;
    top: 92px;
    text-align: right;
  }
  .identity__name {
    color: var(--orange);
    font-weight: 700;
    font-size: 22px;
    letter-spacing: 1px;
    text-transform: uppercase;
  }
  .identity__title {
    color: var(--text-muted);
    font-size: 13px;
    margin-top: 3px;
  }
  .divider {
    position: absolute;
    left: 268px;
    top: 70px;
    width: 1px;
    height: 110px;
    background: var(--divider);
  }
  .contacts {
    position: absolute;
    left: 288px;
    top: 68px;
    list-style: none;
  }
  .contacts li {
    display: flex;
    align-items: center;
    gap: 10px;
    color: var(--text-light);
    font-size: 12.5px;
    line-height: 22px;
  }
  .contacts svg { width: 12px; height: 12px; flex: none; }
  .address {
    position: absolute;
    left: 0; right: 0;
    bottom: 46px;
    display: flex;
    justify-content: center;
    align-items: center;
    gap: 8px;
    color: var(--text-light);
    font-size: 12.5px;
  }
  .address svg { width: 12px; height: 14px; }
  /* brand side */
  .brand {
    position: absolute;
    top: 48px;
    left: 0; right: 0;
    text-align: center;
    color: var(--orange);
    font-weight: 700;
    font-size: 30px;
    letter-spacing: 1px;
  }
  .signage {
    position: absolute;
    left: 40px; right: 40px;
    top: 128px;
    height: 140px;
    border-radius: 8px;
    background: linear-gradient(90deg, #3a2a24 0%, #2a2f3a 45%, #25344a 100%);
  }
</style>
</head>
<body>
  <section class="card card--contact">
    <div class="identity">
      <div class="identity__name">Daniel Reyes</div>
      <div class="identity__title">President</div>
    </div>
    <div class="divider"></div>
    <ul class="contacts">
      <li><svg viewBox="0 0 12 12"><path d="M2 1l2 0 1 3-1.5 1a6 6 0 0 0 3.5 3.5L8 7l3 1v2a1 1 0 0 1-1 1A9 9 0 0 1 1 2a1 1 0 0 1 1-1z" fill="var(--orange)"/></svg>555-214-7731</li>
      <li><svg viewBox="0 0 12 12"><rect x="3" y="0.5" width="6" height="11" rx="1" fill="none" stroke="var(--orange)" stroke-width="1.2"/></svg>555-618-2094</li>
      <li><svg viewBox="0 0 12 12"><rect x="1" y="4" width="10" height="7" rx="1" fill="var(--orange)"/><rect x="3" y="1" width="6" height="3" fill="var(--orange)"/></svg>555-340-6182</li>
      <li><svg viewBox="0 0 12 12"><rect x="0.5" y="2" width="11" height="8" rx="1" fill="var(--orange)"/><path d="M1 3l5 4 5-4" stroke="var(--card)" fill="none"/></svg>daniel@rivexmanagement.com</li>
      <li><svg viewBox="0 0 12 12"><circle cx="6" cy="6" r="5.5" fill="var(--orange)"/><path d="M0.5 6h11M6 0.5c-3 3-3 8 0 11M6 0.5c3 3 3 8 0 11" stroke="var(--card)" fill="none" stroke-width="0.8"/></svg>www.rivexmanagement.com</li>
    </ul>
    <div class="address">
      <svg viewBox="0 0 12 14"><path d="M6 0a5 5 0 0 1 5 5c0 4-5 9-5 9S1 9 1 5a5 5 0 0 1 5-5z" fill="var(--orange)"/><circle cx="6" cy="5" r="2" fill="var(--card)"/></svg>
      4812 Juniper Lane, Fairview, Alaska 34410
    </div>
  </section>

  <section class="card card--brand">
    <div class="brand">Rivex Management LLC</div>
    <div class="signage" role="img" aria-label="Illustrated row of traffic lights, lane arrows, railway crossing and blue road signs"></div>
  </section>
</body>
</html>
```